Flyer-Design für Hypnose
The designer had very good ideas! The design was completly different and absolutely convincing - great! Thank you very much!
Zielgruppe
Hypnose
Aufgabenstellung
Text Vorder- und Rückseite siehe Anlage
Auf der Vorderseite Foto und Logo (auch in der Anlage)
Farbgestaltung passend zu den Logofarben
Das Design soll kreativ und freundlich sein

```html
<!DOCTYPE html>
<html lang="de">
<head>
<meta charset="utf-8">
<title>calmtide Hypnose – Flyer</title>
<link href="https://fonts.googleapis.com/css2?family=Lato:wght@300;400;700;900&display=swap" rel="stylesheet">
<style>
  :root {
    --stage: #9d9c9d;
    --paper: #f3f1f0;
    --rose: #f4b6b1;
    --rose-text: #fdf1ef;
    --brand-orange: #e8582b;
    --photo-sky: #e9ecef;
    --photo-mid: #c9b9a8;
    --photo-skin: #f6c7bd;
    --photo-coat: #f7a997;
  }
  * { box-sizing: border-box; margin: 0; padding: 0; }
  html, body { width: 1200px; height: 1146px; overflow: hidden; }
  body {
    background: var(--stage);
    font-family: "Lato", "Gill Sans", sans-serif;
    position: relative;
  }
  .flyer {
    position: absolute;
    top: 14px;
    width: 559px;
    height: 1116px;
    background: var(--paper);
    padding: 12px 11px;
  }
  .flyer--front { left: 38px; }
  .flyer--back { left: 608px; }
  .flyer__inner {
    position: relative;
    width: 100%;
    height: 100%;
    overflow: hidden;
  }

  /* Front */
  .portrait {
    position: absolute;
    inset: 0 0 125px 0;
    background:
      radial-gradient(ellipse 38% 30% at 48% 40%, var(--photo-skin) 0%, rgba(246,199,189,0) 100%),
      radial-gradient(ellipse 70% 45% at 50% 88%, var(--photo-coat) 0%, rgba(247,169,151,0) 100%),
      linear-gradient(180deg, var(--photo-sky) 0%, #c8ccd0 18%, var(--photo-mid) 45%, #b8a28a 70%, #d9a999 100%);
  }
  .front-brand {
    position: absolute;
    left: 0; right: 0;
    top: 662px;
    text-align: center;
    color: var(--brand-orange);
    font-weight: 700;
  }
  .front-brand__name { font-size: 72px; line-height: 1; letter-spacing: 3px; }
  .front-brand__sub { font-size: 28px; letter-spacing: 7px; margin-top: 6px; }
  .front-footer {
    position: absolute;
    left: 0; right: 0; bottom: 0;
    height: 125px;
    background: var(--rose);
    color: var(--rose-text);
    text-align: center;
    padding-top: 12px;
  }
  .front-footer__name { font-size: 19px; font-weight: 700; line-height: 24px; }
  .front-footer__title { font-size: 19px; font-weight: 300; line-height: 24px; margin-top: 4px; }
  .front-footer__url { font-size: 36px; font-weight: 300; line-height: 42px; margin-top: 4px; letter-spacing: 0.5px; }

  /* Back */
  .flyer--back .flyer__inner {
    background: var(--rose);
    color: var(--rose-text);
    text-align: center;
  }
  .back-brand {
    position: absolute;
    left: 0; right: 0;
    top: 165px;
    font-weight: 700;
  }
  .back-brand__name { font-size: 56px; line-height: 1; letter-spacing: 3px; }
  .back-brand__sub { font-size: 22px; letter-spacing: 6px; margin-top: 6px; }
  .section-title {
    font-size: 27px;
    font-weight: 400;
    line-height: 32px;
  }
  .copy {
    font-size: 15px;
    font-weight: 300;
    line-height: 22.6px;
    padding: 0 16px;
  }
  .intro-title { position: absolute; left: 0; right: 0; top: 280px; }
  .intro-copy { position: absolute; left: 0; right: 0; top: 318px; }
  .topics {
    position: absolute; left: 0; right: 0; top: 408px;
    list-style: none;
    font-size: 15.5px; font-weight: 300; line-height: 22.6px;
  }
  .about-title { position: absolute; left: 0; right: 0; top: 750px; }
  .about-copy { position: absolute; left: 0; right: 0; top: 789px; }
  .slogan {
    position: absolute; left: 0; right: 0; top: 932px;
    font-size: 28px; font-weight: 700; line-height: 31px;
  }
  .slogan__tag { font-size: 15.5px; font-weight: 300; line-height: 20px; display: block; }
  .contact {
    position: absolute; left: 0; right: 0; top: 1033px;
    font-size: 15.5px; font-weight: 300; line-height: 22.6px;
  }
</style>
</head>
<body>
  <section class="flyer flyer--front">
    <div class="flyer__inner">
      <div class="portrait" role="img" aria-label="Foto der Hypnosetrainerin in rosa Jacke und Schal, lächelnd im Freien sitzend"></div>
      <div class="front-brand">
        <div class="front-brand__name">calmtide</div>
        <div class="front-brand__sub">HYPNOSE</div>
      </div>
      <div class="front-footer">
        <p class="front-footer__name">Mag. Lena Plinkwerk, BEd MSc</p>
        <p class="front-footer__title">Diplomierte Hypnosetrainerin</p>
        <p class="front-footer__url">calmtide-hypnose.at</p>
      </div>
    </div>
  </section>

  <section class="flyer flyer--back">
    <div class="flyer__inner">
      <div class="back-brand">
        <div class="back-brand__name">calmtide</div>
        <div class="back-brand__sub">HYPNOSE</div>
      </div>

      <h2 class="section-title intro-title">Wie Hypnose Ihr Leben verändert</h2>
      <p class="copy intro-copy">Hypnose ist eine wunderbare Möglichkeit, das eigene Leben zu verbes&shy;sern. Die Anwendungsbereiche sind unglaublich vielfältig – wenn einer der folgenden Punkte auf Sie zutrifft, sind Sie bei mir richtig:</p>

      <ul class="topics">
        <li>Wunsch mit dem Rauchen aufzuhören</li>
        <li>Wunsch abzunehmen</li>
        <li>Prüfungsangst/Lernblockaden</li>
        <li>Höhenangst</li>
        <li>Platzangst</li>
        <li>Flugangst</li>
        <li>Unsicherheit in Menschenmengen</li>
        <li>Wohlbefinden steigern und Entspannung finden</li>
        <li>Schlafstörungen</li>
        <li>Frust</li>
        <li>Trauer</li>
        <li>Erschöpfung/Überforderung</li>
        <li>Lampenfieber</li>
        <li>Selbstvertrauen steigern</li>
      </ul>

      <h2 class="section-title about-title">Was ist Hypnose?</h2>
      <p class="copy about-copy">Hypnose ist ein Zustand tiefer Entspannung der genutzt werden kann, um erwünschte Gewohnheiten und Handlungsmuster zu verstärken oder unerwünschte aufzulösen. Zusätzlich ist Hypnose hervorragend geeignet, bei Stress oder Überforderung für innere Ruhe und Wohlbe&shy;finden zu sorgen.</p>

      <p class="slogan">Sie brauchen nicht daran zu glauben,<br>Sie brauchen es nur zuzulassen.
        <span class="slogan__tag">Sie werden begeistert sein!</span>
      </p>

      <p class="contact">Kontakt: 0670/5528190, info@calmtide-hypnose.at<br>Am Lindenweg 14, 2351 Mühlbach</p>
    </div>
  </section>
</body>
</html>
```